Daily special re designs for Hospitality Business / Brewery

Need our daily special social images redone - details as follow and examples attached

I am looking to get an Instagram Square, Facebook Event Cover done for the following promotions:

Meat Free Mondays
Tuesday Scnhitty & Beer for $10.48
Wednesdays - $1 Chicken Wings
Thursdays $15 Pizzas
Friday Burger & Beer for $10.48 12-2pm.
Saturday Half Priced Burgers 12-2pm
Sunday $15 Cocktail Jugs & Live Music

Also need a A3 poster of all the deals combined for in venue use and also a newspaper ad 260mm w x 92mm h

```html
<!DOCTYPE html>
<html lang="en">
<head>
<meta charset="utf-8">
<title>Redgum Flats Brewing Co – Meat-Free Mondays</title>
<link rel="stylesheet" href="https://fonts.googleapis.com/css2?family=Montserrat:wght@700&family=Lobster&family=Great+Vibes&display=swap">
<style>
  :root {
    --bg-dark: #151515;
    --photo-deep: #1c1c1c;
    --photo-veg-green: #3d5a2a;
    --photo-veg-red: #7a2418;
    --photo-veg-yellow: #8a6a22;
    --photo-cloth: #8a6a2a;
    --panel: rgba(8, 8, 8, 0.78);
    --panel-border: rgba(255, 255, 255, 0.75);
    --white: #ffffff;
    --outline: #000000;
    --green: #1fa34f;
  }
  * { margin: 0; padding: 0; box-sizing: border-box; }
  html, body {
    width: 1200px;
    height: 1200px;
    overflow: hidden;
    background: var(--bg-dark);
  }
  .promo {
    position: relative;
    width: 1200px;
    height: 1200px;
    overflow: hidden;
  }
  .promo__photo {
    position: absolute;
    inset: 0;
    background:
      radial-gradient(ellipse 30% 22% at 95% 8%, var(--photo-cloth) 0%, transparent 100%),
      radial-gradient(ellipse 12% 14% at 3% 88%, var(--photo-veg-red) 0%, transparent 100%),
      radial-gradient(ellipse 28% 22% at 40% 45%, var(--photo-veg-green) 0%, transparent 100%),
      radial-gradient(ellipse 26% 24% at 60% 62%, var(--photo-veg-red) 0%, transparent 100%),
      radial-gradient(ellipse 22% 18% at 50% 78%, var(--photo-veg-yellow) 0%, transparent 100%),
      radial-gradient(circle at 50% 55%, #2a2a2a 0%, var(--photo-deep) 60%, #101010 100%);
  }
  .promo__panel {
    position: absolute;
    left: 98px;
    top: 244px;
    width: 1005px;
    height: 850px;
    border-radius: 34px;
    border: 1.5px solid var(--panel-border);
    background: var(--panel);
  }
  .brand {
    position: absolute;
    top: 150px;
    left: 0;
    width: 100%;
    text-align: center;
    font-family: "Montserrat", sans-serif;
    font-weight: 700;
    color: var(--white);
    letter-spacing: 4px;
    line-height: 1.25;
  }
  .brand__name { font-size: 52px; display: block; }
  .brand__sub { font-size: 44px; display: block; margin-top: 8px; }
  .headline {
    position: absolute;
    top: 590px;
    left: 0;
    width: 100%;
    text-align: center;
  }
  .headline__script {
    display: block;
    font-family: "Lobster", cursive;
    font-size: 112px;
    line-height: 1;
    color: var(--white);
    -webkit-text-stroke: 4px var(--outline);
    paint-order: stroke fill;
  }
  .headline__day {
    display: block;
    font-family: "Montserrat", sans-serif;
    font-weight: 700;
    font-size: 166px;
    line-height: 1;
    letter-spacing: 2px;
    color: var(--green);
    margin-top: 4px;
  }
  .tagline {
    position: absolute;
    top: 920px;
    left: 0;
    width: 100%;
    text-align: center;
    font-family: "Great Vibes", cursive;
    font-size: 62px;
    color: var(--white);
  }
</style>
</head>
<body>
  <main class="promo">
    <div class="promo__photo" role="img" aria-label="Top-down photo of a dark pan of colourful stir-fried vegetables with forks, cherry tomatoes and a mustard napkin"></div>
    <div class="promo__panel"></div>
    <header class="brand">
      <span class="brand__name">REDGUM FLATS</span>
      <span class="brand__sub">BREWING CO</span>
    </header>
    <h1 class="headline">
      <span class="headline__script">Meat-Free</span>
      <span class="headline__day">MONDAYS</span>
    </h1>
    <p class="tagline">Great Vegetarian and Vegan Specials</p>
  </main>
</body>
</html>
```